Need a logo and business card design for my electrical company.
Company name is Kestrel Volt Electrical
In the bottow right hand corner i need
E.C. 708291 for the momument till i get my contractors license number sent to me.
Design i want black back ground with a picture of Thor's hammer and lighting hitting the top of it.

Industry/Entity Type

Electrical

Contact Information for Business Card

Owner Dermot Ashby Phone number 0412873590 email kestrelvoltelectrical@wirepostmail.com facebook page Kestrel Volt Electrical

```html
<!DOCTYPE html>
<html lang="en">
<head>
<meta charset="utf-8">
<title>Kestrel Volt Electrical – Business Card</title>
<link rel="stylesheet" href="https://fonts.googleapis.com/css2?family=Arimo:wght@400;700&display=swap">
<style>
  :root {
    --page-bg: #e9e6e1;
    --card-bg: #000000;
    --ink: #ffffff;
    --brand-blue: #1f8fff;
    --bolt-light: #3fc6f0;
    --bolt-deep: #1536c8;
    --band-edge: #0a1a78;
    --band-mid: #0f5f6a;
  }
  * { box-sizing: border-box; margin: 0; padding: 0; }
  html, body {
    width: 1200px;
    height: 851px;
    overflow: hidden;
    background: var(--page-bg);
    font-family: "Arimo", Arial, sans-serif;
  }
  .card {
    position: absolute;
    left: 100px;
    top: 118px;
    width: 1000px;
    height: 616px;
    background: var(--card-bg);
    overflow: hidden;
    box-shadow: 0 6px 18px rgba(0,0,0,0.35);
  }
  .lightning-art {
    position: absolute;
    left: 0;
    top: 0;
    width: 205px;
    height: 616px;
    background: linear-gradient(100deg, rgba(21,54,200,0.55) 0%, rgba(63,198,240,0.35) 45%, rgba(0,0,0,0) 100%);
  }
  .brand {
    position: absolute;
    left: 200px;
    top: 130px;
    width: 280px;
    display: flex;
    flex-direction: column;
    align-items: center;
    gap: 18px;
  }
  .brand-mark {
    width: 120px;
    height: 120px;
    border-radius: 50%;
    border: 14px solid var(--brand-blue);
  }
  .brand-name {
    color: var(--brand-blue);
    font-weight: 700;
    font-size: 26px;
    text-align: center;
    line-height: 1.15;
  }
  .owner-name {
    position: absolute;
    right: 91px;
    top: 128px;
    color: var(--ink);
    font-weight: 700;
    font-size: 32px;
  }
  .contact-list {
    position: absolute;
    right: 91px;
    top: 190px;
    list-style: none;
  }
  .contact-item {
    display: flex;
    align-items: center;
    justify-content: flex-end;
    gap: 28px;
    height: 42px;
    margin-bottom: 20.5px;
    color: var(--ink);
    font-size: 27px;
  }
  .contact-icon {
    width: 42px;
    height: 42px;
    flex: none;
  }
  .licence-band {
    position: absolute;
    left: 0;
    top: 503px;
    width: 1000px;
    height: 54px;
    background: linear-gradient(90deg, var(--band-edge) 0%, var(--band-mid) 50%, var(--band-edge) 100%);
  }
  .licence-number {
    position: absolute;
    right: 91px;
    top: 50%;
    transform: translateY(-50%);
    color: var(--ink);
    font-size: 30px;
  }
</style>
</head>
<body>
  <main class="card">
    <div class="lightning-art" role="img" aria-label="Blue forked lightning bolts branching down the left edge"></div>

    <div class="brand">
      <div class="brand-mark"></div>
      <p class="brand-name">Kestrel Volt Electrical</p>
    </div>

    <h1 class="owner-name">Dermot Ashby</h1>

    <ul class="contact-list">
      <li class="contact-item">
        <span>Phone number</span>
        <svg class="contact-icon" viewBox="0 0 42 42" aria-hidden="true">
          <circle cx="21" cy="21" r="19" fill="none" stroke="var(--ink)" stroke-width="2.5"/>
          <path d="M15 11c-2 1-3 3-2 6 2 6 6 11 12 14 2 1 4 0 5-2l-4-4-3 2c-3-2-5-4-6-7l2-3z" fill="var(--ink)"/>
        </svg>
      </li>
      <li class="contact-item">
        <span>Email address</span>
        <svg class="contact-icon" viewBox="0 0 42 42" aria-hidden="true">
          <rect x="4" y="11" width="34" height="21" rx="2" fill="var(--ink)"/>
          <path d="M5 12l16 12 16-12" fill="none" stroke="var(--card-bg)" stroke-width="2"/>
        </svg>
      </li>
      <li class="contact-item">
        <span>www.company.com</span>
        <svg class="contact-icon" viewBox="0 0 42 42" aria-hidden="true">
          <g fill="none" stroke="var(--ink)" stroke-width="2.5">
            <circle cx="21" cy="21" r="18"/>
            <ellipse cx="21" cy="21" rx="8" ry="18"/>
            <line x1="21" y1="3" x2="21" y2="39"/>
            <line x1="3" y1="21" x2="39" y2="21"/>
            <path d="M6 12h30M6 30h30"/>
          </g>
        </svg>
      </li>
      <li class="contact-item">
        <span>Local address</span>
        <svg class="contact-icon" viewBox="0 0 42 42" aria-hidden="true">
          <path d="M21 5L3 17h36z" fill="var(--ink)"/>
          <rect x="7" y="17" width="28" height="20" fill="var(--ink)"/>
          <rect x="12" y="22" width="7" height="7" fill="var(--card-bg)"/>
          <rect x="23" y="22" width="7" height="7" fill="var(--card-bg)"/>
        </svg>
      </li>
    </ul>

    <div class="licence-band">
      <span class="licence-number">E.C. 708291</span>
    </div>
  </main>
</body>
</html>
```